The Marlowe Legal Group, P.C.
Business Cards, Stationary & Email Signature & Letterhead
Use same font as used in my logo
Ruth Benning
Attorney
2847 Tamworth Lane
Suite 3405
Kennesaw, GA 30582
ruthbenningesq@quillpost.net
www.marlowelegaloffice.com
Logo + whatever
Ai file of my logo for Stationary project

```html
<!DOCTYPE html>
<html lang="en">
<head>
<meta charset="utf-8">
<title>The Marlowe Legal Group, P.C. — Stationery</title>
<link href="https://fonts.googleapis.com/css2?family=EB+Garamond:wght@500&family=Open+Sans:wght@400;600&display=swap" rel="stylesheet">
<style>
:root{
  --bg:#ece6dc;
  --paper:#ffffff;
  --navy:#1d3d8c;
  --navy-deep:#0f2b6b;
  --navy-light:#3f68bf;
  --grey:#8b909a;
  --grey-light:#d9dce2;
  --text:#4a4f59;
}
*{margin:0;padding:0;box-sizing:border-box}
html,body{width:1200px;height:698px;overflow:hidden}
body{background:var(--bg);position:relative;font-family:"Open Sans",Arial,sans-serif;color:var(--text)}
.piece{position:absolute;background:var(--paper);box-shadow:0 2px 6px rgba(0,0,0,.18);overflow:hidden}
.wave{position:absolute;left:0;bottom:0;width:100%}
.logo{display:flex;align-items:center;gap:5px}
.logo .mark{border-radius:50%;border:2px solid var(--navy);flex:none}
.logo .name{font-family:"EB Garamond",Georgia,serif;font-weight:500;color:var(--navy);line-height:1.05}
.logo.light .mark{border-color:#fff}
.logo.light .name{color:#fff}
.divider{width:1px;background:var(--grey-light);align-self:stretch}
.small{font-size:5px;line-height:1.45;color:var(--grey)}
.person{font-family:"EB Garamond",Georgia,serif;color:var(--navy);font-weight:500}
.role{font-size:5px;color:var(--grey);text-transform:uppercase;letter-spacing:.5px}

/* business cards */
.card-front{left:65px;top:79px;width:187px;height:113px}
.card-front .logo{position:absolute;left:10px;top:12px}
.card-front .info{position:absolute;left:98px;top:12px}
.card-name{left:269px;top:79px;width:187px;height:113px;text-align:center}
.card-name .info{padding-top:10px}
.card-name .logo{justify-content:center;margin-top:8px}
.card-blue{left:65px;top:199px;width:187px;height:98px;background:radial-gradient(circle at 50% 45%,var(--navy-light),var(--navy-deep) 75%);display:flex;align-items:center;justify-content:center}
.card-plain{left:269px;top:199px;width:187px;height:98px;background:linear-gradient(160deg,#fff 40%,#e4e6ea);display:flex;align-items:center;justify-content:center}

/* letterhead */
.letterhead{left:566px;top:79px;width:262px;height:341px}
.letterhead .head,.fax .head{position:absolute;left:16px;top:16px;display:flex;gap:8px;height:26px}
.letterhead .foot,.fax .foot{position:absolute;bottom:10px;width:100%;text-align:center;font-size:4.5px;color:var(--grey)}

/* fax */
.fax{left:840px;top:79px;width:264px;height:341px}
.fax-title{position:absolute;right:16px;top:56px;font-weight:600;font-size:11px;color:var(--navy);letter-spacing:.5px}
.fax-table{position:absolute;left:16px;right:16px;top:70px;display:grid;grid-template-columns:1fr 1fr;gap:1px;background:#fff;border:1px solid var(--grey-light)}
.fax-table div{background:#eceef1;height:12px;font-size:5px;line-height:12px;padding-left:4px;color:var(--grey)}
.fax-checks{position:absolute;left:16px;right:16px;top:126px;display:flex;justify-content:space-between;font-size:4.5px;color:var(--grey)}
.fax-checks span::before{content:"";display:inline-block;width:4px;height:4px;border:.6px solid var(--grey);margin-right:2px;vertical-align:-0.5px}
.fax-comments{position:absolute;left:16px;top:138px;font-size:4.5px;color:var(--grey)}

/* envelopes */
.env-back{left:139px;top:384px;width:262px;height:108px}
.env-back svg.flap{position:absolute;left:0;top:0}
.env-back .logo{position:absolute;left:50%;top:12px;transform:translateX(-50%)}
.env-front{left:139px;top:509px;width:262px;height:115px}
.env-front .head{position:absolute;left:10px;top:10px;display:flex;gap:7px;height:22px}

/* email signatures */
.sig-wide{left:552px;top:545px;width:319px;height:74px;display:flex;align-items:center;gap:10px;padding:0 12px}
.sig-card{left:883px;top:533px;width:221px;height:96px}
.sig-card .logo{position:absolute;left:12px;top:12px}
.sig-card .info{position:absolute;left:118px;top:14px}
</style>
</head>
<body>

<!-- Business card: logo and details -->
<div class="piece card-front">
  <div class="logo"><span class="mark" style="width:14px;height:14px"></span><span class="name" style="font-size:10px;width:70px">The Marlowe Legal Group, P.C.</span></div>
  <div class="info">
    <div class="person" style="font-size:8px">Ruth Benning</div>
    <div class="role">Attorney</div>
    <div class="small" style="margin-top:4px">2847 Tamworth Lane<br>Suite 3405<br>Kennesaw, GA 30582<br>Tel 555.014.2210<br>ruthbenningesq@quillpost.net<br>www.marlowelegaloffice.com</div>
  </div>
  <svg class="wave" viewBox="0 0 187 20" height="20" preserveAspectRatio="none"><path d="M0 10 Q60 0 120 8 T187 4 V20 H0Z" fill="var(--grey-light)"/><path d="M0 14 Q70 4 130 12 T187 9 V20 H0Z" fill="var(--navy)"/></svg>
</div>

<!-- Business card: name and logo -->
<div class="piece card-name">
  <div class="info">
    <div class="person" style="font-size:8px">Ruth Benning</div>
    <div class="role">Attorney</div>
  </div>
  <div class="logo"><span class="mark" style="width:16px;height:16px"></span><span class="name" style="font-size:12px;width:90px;text-align:left">The Marlowe Legal Group, P.C.</span></div>
  <svg class="wave" viewBox="0 0 187 20" height="20" preserveAspectRatio="none"><path d="M0 10 Q60 0 120 8 T187 4 V20 H0Z" fill="var(--grey-light)"/><path d="M0 14 Q70 4 130 12 T187 9 V20 H0Z" fill="var(--navy)"/></svg>
</div>

<!-- Business card: blue back -->
<div class="piece card-blue">
  <div class="logo light"><span class="mark" style="width:18px;height:18px"></span><span class="name" style="font-size:13px;width:95px">The Marlowe Legal Group, P.C.</span></div>
</div>

<!-- Business card: white back -->
<div class="piece card-plain">
  <div class="logo"><span class="mark" style="width:18px;height:18px"></span><span class="name" style="font-size:13px;width:95px">The Marlowe Legal Group, P.C.</span></div>
</div>

<!-- Letterhead -->
<div class="piece letterhead">
  <div class="head">
    <div class="logo"><span class="mark" style="width:14px;height:14px"></span><span class="name" style="font-size:10px;width:70px">The Marlowe Legal Group, P.C.</span></div>
    <span class="divider"></span>
    <div class="small">2847 Tamworth Lane, Suite 3405<br>Kennesaw, GA 30582<br>Tel 555.014.2210</div>
  </div>
  <div class="foot">www.marlowelegaloffice.com</div>
</div>

<!-- Fax cover -->
<div class="piece fax">
  <div class="head">
    <div class="logo"><span class="mark" style="width:14px;height:14px"></span><span class="name" style="font-size:10px;width:70px">The Marlowe Legal Group, P.C.</span></div>
    <span class="divider"></span>
    <div class="small">2847 Tamworth Lane, Suite 3405<br>Kennesaw, GA 30582<br>Tel 555.014.2210</div>
  </div>
  <div class="fax-title">FAX</div>
  <div class="fax-table">
    <div>To</div><div>From</div>
    <div>Fax</div><div>Pages</div>
    <div>Phone</div><div>Date</div>
    <div>Re</div><div>CC</div>
  </div>
  <div class="fax-checks"><span>Urgent</span><span>For Review</span><span>Please Comment</span><span>Please Reply</span><span>Please Recycle</span></div>
  <div class="fax-comments">Comments:</div>
  <div class="foot">www.marlowelegaloffice.com</div>
</div>

<!-- Envelope back -->
<div class="piece env-back">
  <svg class="flap" width="262" height="108" viewBox="0 0 262 108"><path d="M0 0 L131 46 L262 0" fill="none" stroke="var(--grey-light)" stroke-width="1"/></svg>
  <div class="logo"><span class="mark" style="width:16px;height:16px"></span></div>
</div>

<!-- Envelope front -->
<div class="piece env-front">
  <div class="head">
    <div class="logo"><span class="mark" style="width:13px;height:13px"></span><span class="name" style="font-size:9px;width:64px">The Marlowe Legal Group, P.C.</span></div>
    <span class="divider"></span>
    <div class="small">2847 Tamworth Lane, Suite 3405<br>Kennesaw, GA 30582<br>Tel 555.014.2210</div>
  </div>
</div>

<!-- Email signature: wide -->
<div class="piece sig-wide">
  <div class="logo"><span class="mark" style="width:16px;height:16px"></span><span class="name" style="font-size:12px;width:92px">The Marlowe Legal Group, P.C.</span></div>
  <span class="divider"></span>
  <div>
    <div class="person" style="font-size:8px">Ruth Benning</div>
    <div class="role">Attorney</div>
  </div>
  <span class="divider"></span>
  <div class="small">2847 Tamworth Lane, Suite 3405<br>Kennesaw, GA 30582<br>Tel 555.014.2210<br>ruthbenningesq@quillpost.net<br>www.marlowelegaloffice.com</div>
</div>

<!-- Email signature: card style -->
<div class="piece sig-card">
  <div class="logo"><span class="mark" style="width:14px;height:14px"></span><span class="name" style="font-size:10px;width:75px">The Marlowe Legal Group, P.C.</span></div>
  <div class="info">
    <div class="person" style="font-size:8px">Ruth Benning</div>
    <div class="role">Attorney</div>
    <div class="small" style="margin-top:3px">2847 Tamworth Lane<br>Suite 3405<br>Kennesaw, GA 30582<br>ruthbenningesq@quillpost.net<br>www.marlowelegaloffice.com</div>
  </div>
  <svg class="wave" viewBox="0 0 221 16" height="16" preserveAspectRatio="none"><path d="M0 8 Q70 0 140 6 T221 3 V16 H0Z" fill="var(--grey-light)"/><path d="M0 11 Q80 3 150 9 T221 7 V16 H0Z" fill="var(--navy)"/></svg>
</div>

</body>
</html>
```